The Verdant Ledger App - Modernization & Graphics User Interface Friendliness Updates

We are Verdant Ledger, and we want to bring a new branding look and graphical user interface to the Verdant Ledger App. The app is a quick reference encyclopedia for all things produce. Boasting articles on over 2,000 produce items, with information ranging from taste and application to geographical and cultural significance. Included in its features are over 10 thousand recipes, and the Verdant Ledger App Harvest Circle – a global initiative to connect farmer, customer, and chef in one sustainable and easy to use application. The design needs to bring a greater sense of social connection – encouraging the user to participate in the 'Harvest Circled' experience voluntarily. The design should reflect a sense of authority reflecting the authenticity and reliability of the provided information, it's writing, and its sources. Download the App here: vledgr.example/install

Target Market(s)

Women and Men between ages 21-55.

Industry/Entity Type

Education

Font styles to use
Serif
Sans Serif

Colors

Designer to choose colors to be used in the design.

Requirements
Must have
• An updated user interface, the intuitive usability of the app is currently non-existent. We are looking to reflect as the authority on produce. The app design must reflect a professional, user-friendly, up-to-date, and trustworthy feel.
Nice to have
• To incorporate the social draw of the Harvest Circle we would like to include on the home page "Social Bubbles" (think Pictoloop stories) which updates with shared photos of produce and their location.
Should not have
• An overly complicated theme, distracting or unprofessional colors, and images.

```html
<!DOCTYPE html>
<html lang="en">
<head>
<meta charset="utf-8">
<title>Verdant Ledger App – Screens</title>
<link rel="stylesheet" href="https://fonts.googleapis.com/css2?family=Montserrat:wght@400;500;600;700&family=Open+Sans:ital,wght@0,300;0,400;1,300;1,400&display=swap">
<style>
  :root {
    --bg: #f7f7f8;
    --screen: #ffffff;
    --ink: #222222;
    --muted: #8a8a8a;
    --faint: #b5b5b5;
    --green: #5bcd3a;
    --rule: #e6e6e6;
    --panel: #f3f3f3;
    --frame: #2a2a2a;
  }
  * { box-sizing: border-box; margin: 0; padding: 0; }
  html, body { width: 1200px; height: 1008px; overflow: hidden; background: var(--bg); }
  body { position: relative; font-family: "Montserrat", sans-serif; color: var(--ink); }

  .screen { position: absolute; top: 208px; width: 318px; height: 562px; background: var(--screen); overflow: hidden; outline: 1px solid var(--frame); }
  .screen--home { left: 54px; }
  .screen--produce { left: 436px; }
  .screen--detail { left: 817px; }
  .abs { position: absolute; }

  .status-bar { position: absolute; top: 0; left: 0; right: 0; height: 16px; font-size: 10px; font-family: "Open Sans", sans-serif; display: flex; align-items: center; justify-content: space-between; padding: 0 6px; }
  .status-bar .carrier, .status-bar .power { display: flex; align-items: center; gap: 3px; }
  .status-bar .clock { position: absolute; left: 0; right: 0; text-align: center; pointer-events: none; }

  .app-header { position: absolute; top: 16px; left: 0; right: 0; height: 35px; display: flex; align-items: center; justify-content: space-between; padding: 0 14px 0 15px; }
  .app-header h1 { position: absolute; left: 0; right: 0; text-align: center; font-size: 14px; font-weight: 700; letter-spacing: 1px; pointer-events: none; }

  /* Home */
  .market-band { position: absolute; top: 51px; left: 0; right: 0; height: 118px; background: linear-gradient(180deg, #2e2e2e 0%, #3a3634 30%, #6a4a30 55%, #8a5f3a 100%); }
  .market-band .band-title { position: absolute; top: 13px; left: 11px; font-size: 8.5px; font-weight: 500; color: #fff; letter-spacing: .2px; }
  .see-all { font-size: 8px; font-weight: 600; color: var(--green); letter-spacing: .3px; }
  .market-band .see-all { position: absolute; top: 14px; right: 10px; }
  .bubble { position: absolute; top: 36px; width: 48px; height: 48px; border-radius: 50%; border: 2px solid #fff; }
  .bubble--create { background: #fff; border-color: var(--green); display: flex; align-items: center; justify-content: center; }
  .bubble-label { position: absolute; top: 91px; width: 70px; text-align: center; font-size: 8px; color: #fff; line-height: 1.2; }
  .bubble-label--create { color: var(--green); }

  .section-title { position: absolute; left: 14px; font-size: 12px; font-weight: 600; }
  .feature-name { position: absolute; top: 204px; left: 21px; font-size: 23px; font-weight: 700; line-height: 27px; color: #333; }
  .feature-meta { position: absolute; top: 267px; left: 21px; font-size: 8px; line-height: 10px; color: #666; font-family: "Open Sans", sans-serif; }
  .btn-outline { position: absolute; top: 316px; left: 21px; width: 57px; height: 22px; border: 1.5px solid var(--green); border-radius: 11px; font-size: 8px; font-weight: 600; color: var(--green); display: flex; align-items: center; justify-content: center; }
  .pager { position: absolute; top: 323px; left: 182px; display: flex; gap: 4px; }
  .pager span { width: 4px; height: 4px; border-radius: 50%; background: #ccc; }
  .pager span.is-current { background: var(--green); }
  .divider { position: absolute; left: 0; right: 0; height: 1px; background: var(--rule); }
  .produce-thumb { position: absolute; top: 388px; width: 80px; height: 82px; background: #fafafa; }
  .produce-label { position: absolute; top: 478px; width: 80px; font-size: 9px; line-height: 11px; color: #333; }

  .tab-bar { position: absolute; top: 518px; left: 0; right: 0; height: 44px; border-top: 1px solid var(--rule); background: #fff; }
  .tab-bar svg { position: absolute; top: 10px; width: 24px; height: 24px; }

  /* Produce */
  .category-tile { position: absolute; left: 4px; right: 6px; overflow: hidden; }
  .category-tile .tile-art { position: absolute; right: 0; top: 0; bottom: 0; width: 130px; }
  .category-tile h2 { position: absolute; left: 22px; font-size: 20px; font-weight: 700; color: rgba(255,255,255,.92); letter-spacing: .8px; line-height: 24px; text-shadow: 0 1px 3px rgba(0,0,0,.25); }

  /* Detail */
  .item-name { position: absolute; top: 197px; left: 0; right: 0; text-align: center; font-size: 19px; font-weight: 700; color: #333; }
  .item-meta { position: absolute; top: 228px; left: 0; right: 0; text-align: center; font-family: "Open Sans", sans-serif; font-style: italic; font-weight: 300; font-size: 10px; line-height: 14px; color: var(--faint); }
  .stat { position: absolute; top: 280px; width: 70px; text-align: center; }
  .stat svg { width: 22px; height: 22px; display: block; margin: 0 auto 4px; }
  .stat b { display: block; font-size: 11px; font-weight: 600; color: #333; }
  .stat small { display: block; font-size: 8px; color: var(--muted); margin-top: 1px; }
  .description { position: absolute; top: 342px; left: 0; right: 0; height: 176px; background: var(--panel); }
  .description h3 { position: absolute; top: 21px; left: 0; right: 0; text-align: center; font-family: "Open Sans", sans-serif; font-style: italic; font-weight: 400; font-size: 14px; color: #333; }
  .description p { position: absolute; top: 56px; left: 22px; width: 270px; font-family: "Open Sans", sans-serif; font-weight: 300; font-size: 10.5px; line-height: 15.2px; color: #555; }
</style>
</head>
<body>

<svg width="0" height="0" style="position:absolute" aria-hidden="true">
  <defs>
    <symbol id="i-home" viewBox="0 0 24 24"><path d="M2 12 12 3l10 9M5 10v11h5v-6h4v6h5V10" fill="none" stroke="currentColor" stroke-width="1.3" stroke-linejoin="round"/></symbol>
    <symbol id="i-eye" viewBox="0 0 24 24"><path d="M1 12c3-5 7-7 11-7s8 2 11 7c-3 5-7 7-11 7s-8-2-11-7z" fill="none" stroke="currentColor" stroke-width="1.3"/><circle cx="12" cy="12" r="4" fill="none" stroke="currentColor" stroke-width="1.3"/></symbol>
    <symbol id="i-apple" viewBox="0 0 24 24"><path d="M12 7c-2-2-8-2-8 5 0 5 3 10 6 10 1 0 1.5-.5 2-.5s1 .5 2 .5c3 0 6-5 6-10 0-7-6-7-8-5z" fill="none" stroke="currentColor" stroke-width="1.3"/><path d="M12 7c0-2 1-4 3-5" fill="none" stroke="currentColor" stroke-width="1.3"/></symbol>
    <symbol id="i-bowl" viewBox="0 0 24 24"><path d="M2 11h20c0 5-4 9-10 9S2 16 2 11zM8 20v2h8v-2M14 9l7-6M5 8h12" fill="none" stroke="currentColor" stroke-width="1.3" stroke-linejoin="round"/></symbol>
    <symbol id="i-person" viewBox="0 0 24 24"><path d="M12 3c3 0 5 2 5 5 0 3-2 6-5 6s-5-3-5-6c0-3 2-5 5-5zM3 22c0-4 4-6 9-6s9 2 9 6z" fill="none" stroke="currentColor" stroke-width="1.3" stroke-linejoin="round"/></symbol>
    <symbol id="i-menu" viewBox="0 0 24 24"><path d="M2 5h20M2 12h20M2 19h14" stroke="currentColor" stroke-width="2"/></symbol>
    <symbol id="i-search" viewBox="0 0 24 24"><circle cx="10" cy="10" r="8" fill="none" stroke="currentColor" stroke-width="1.6"/><path d="M16 16l6 6" stroke="currentColor" stroke-width="1.6"/></symbol>
    <symbol id="i-signal" viewBox="0 0 12 8"><rect x="0" y="5" width="2" height="3"/><rect x="3" y="3.5" width="2" height="4.5"/><rect x="6" y="2" width="2" height="6"/><rect x="9" y="0" width="2" height="8"/></symbol>
    <symbol id="i-wifi" viewBox="0 0 12 9"><path d="M1 3.5a7 7 0 0 1 10 0M2.8 5.3a4.5 4.5 0 0 1 6.4 0" fill="none" stroke="currentColor" stroke-width="1.2"/><circle cx="6" cy="7.5" r="1"/></symbol>
    <symbol id="i-battery" viewBox="0 0 24 11"><rect x=".5" y=".5" width="21" height="10" rx="1.5" fill="none" stroke="currentColor"/><rect x="2" y="2" width="11" height="7"/><rect x="22" y="3.5" width="1.5" height="4"/></symbol>
  </defs>
</svg>

<!-- Home screen -->
<section class="screen screen--home">
  <div class="status-bar">
    <span class="carrier"><svg width="12" height="8"><use href="#i-signal"/></svg>Nimbus<svg width="12" height="9"><use href="#i-wifi"/></svg></span>
    <span class="clock">9:41 AM</span>
    <span class="power">58 %<svg width="24" height="11"><use href="#i-battery"/></svg></span>
  </div>
  <header class="app-header">
    <svg width="18" height="18"><use href="#i-menu"/></svg>
    <h1>HOME</h1>
    <svg width="22" height="22"><use href="#i-search"/></svg>
  </header>

  <div class="market-band" role="img" aria-label="Dark slate and wooden table backdrop">
    <span class="band-title">RECENTLY SPOTED IN MARKET</span>
    <span class="see-all">SEE ALL</span>
    <div class="bubble bubble--create" style="left:11px"><svg width="22" height="22" viewBox="0 0 22 22"><path d="M11 2v18M2 11h18" stroke="#5bcd3a" stroke-width="2.2"/></svg></div>
    <div class="bubble" style="left:80px;background:radial-gradient(circle,#7ab548,#3f7a2a)" role="img" aria-label="Photo of green shishito chile peppers"></div>
    <div class="bubble" style="left:149px;background:radial-gradient(circle,#e8503a,#a81f1f)" role="img" aria-label="Photo of rambutan fruit"></div>
    <div class="bubble" style="left:218px;background:radial-gradient(circle,#e8dc4a,#b3a21e)" role="img" aria-label="Photo of yellow plumcots"></div>
    <div class="bubble" style="left:287px;background:radial-gradient(circle,#5aa03a,#2f6a22)" role="img" aria-label="Photo of fresh mint"></div>
    <span class="bubble-label bubble-label--create" style="left:0">CREATE</span>
    <span class="bubble-label" style="left:69px">Green Shishito Chile Peppers</span>
    <span class="bubble-label" style="left:138px">Rambutan</span>
    <span class="bubble-label" style="left:207px">Plumcot</span>
    <span class="bubble-label" style="left:276px">Mint</span>
  </div>

  <h2 class="section-title" style="top:179px">Priced to Sell</h2>
  <div class="feature-name">Spring<br>Mix</div>
  <div class="feature-meta">Inventory,<br>3 lbs : 550.00<br>330 restaurant<br>1 recipes</div>
  <div class="abs" style="top:202px;left:120px;width:186px;height:98px;border-radius:50%;background:radial-gradient(ellipse,#4f8a2e 0%,#2f6a22 55%,rgba(255,255,255,0) 72%)" role="img" aria-label="Photo of a heap of spring mix salad greens"></div>
  <div class="btn-outline">SEE ALL</div>
  <div class="pager"><span class="is-current"></span><span></span><span></span><span></span><span></span></div>

  <div class="divider" style="top:348px"></div>
  <h2 class="section-title" style="top:362px;left:11px">Produce available</h2>
  <span class="see-all abs" style="top:366px;right:10px">SEE ALL</span>
  <div class="produce-thumb" style="left:11px;background:radial-gradient(ellipse at 50% 45%,#6b2e3c 0%,#8a4a58 35%,#fafafa 65%)" role="img" aria-label="Photo of champagne grapes"></div>
  <div class="produce-thumb" style="left:99px;background:radial-gradient(ellipse at 50% 50%,#e6c92a 0%,#f0d84a 35%,#fafafa 68%)" role="img" aria-label="Photo of baby yellow patty pan squash"></div>
  <div class="produce-thumb" style="left:187px;background:radial-gradient(ellipse at 50% 50%,#d9912e 0%,#e8a848 38%,#fafafa 68%)" role="img" aria-label="Photo of chanterelle mushrooms"></div>
  <div class="produce-thumb" style="left:275px;background:radial-gradient(ellipse at 60% 50%,#c8242a 0%,#d84040 38%,#fafafa 68%)" role="img" aria-label="Photo of strawberries"></div>
  <span class="produce-label" style="left:11px">Champagne Grapes</span>
  <span class="produce-label" style="left:99px">Baby Yellow Patty Pan Squash</span>
  <span class="produce-label" style="left:187px">Chanterelle Mushrooms</span>
  <span class="produce-label" style="left:275px;white-space:nowrap">Strawberries</span>

  <nav class="tab-bar">
    <svg style="left:23px;color:var(--green)"><use href="#i-home"/></svg>
    <svg style="left:86px;color:#777"><use href="#i-eye"/></svg>
    <svg style="left:148px;color:#777"><use href="#i-apple"/></svg>
    <svg style="left:210px;color:#777"><use href="#i-bowl"/></svg>
    <svg style="left:268px;color:#777"><use href="#i-person"/></svg>
  </nav>
</section>

<!-- Produce screen -->
<section class="screen screen--produce">
  <div class="status-bar">
    <span class="carrier"><svg width="12" height="8"><use href="#i-signal"/></svg>Nimbus<svg width="12" height="9"><use href="#i-wifi"/></svg></span>
    <span class="clock">9:41 AM</span>
    <span class="power">58 %<svg width="24" height="11"><use href="#i-battery"/></svg></span>
  </div>
  <header class="app-header">
    <svg width="18" height="18"><use href="#i-menu"/></svg>
    <h1>PRODUCE</h1>
    <svg width="22" height="22"><use href="#i-search"/></svg>
  </header>

  <div class="category-tile" style="top:52px;height:137px;background:linear-gradient(180deg,#e4e4e4,#cfcfcf)">
    <div class="tile-art" style="background:linear-gradient(200deg,#f39a1c 0%,#8a2a3a 35%,#7cc23a 70%,rgba(207,207,207,0) 100%)" role="img" aria-label="Photo of oranges, grapes, avocado and green apple on white wood"></div>
    <h2 style="top:50px">ALL FRUIT</h2>
  </div>
  <div class="category-tile" style="top:192px;height:134px;background:linear-gradient(160deg,#ececec,#cdcdcd)">
    <div class="tile-art" style="background:linear-gradient(190deg,#d93a2a 0%,#e0402a 35%,#e8782a 65%,#2f5a2a 100%)" role="img" aria-label="Photo of tomatoes, carrots and kale on marble"></div>
    <h2 style="top:50px">ALL<br>VEGETABLES</h2>
  </div>
  <div class="category-tile" style="top:330px;height:134px;background:linear-gradient(135deg,#d8d8d8,#a8a8a8 60%,#c8c8c8)">
    <div class="tile-art" style="background:linear-gradient(200deg,rgba(200,200,200,0) 0%,#6e9a4a 40%,#2f6a22 100%)" role="img" aria-label="Photo of wild herbs and greens on weathered wood"></div>
    <h2 style="top:58px">FORAGED</h2>
  </div>
  <div class="category-tile" style="top:467px;height:60px;background:linear-gradient(135deg,#c9a55a,#a07a38)">
    <div class="tile-art" style="background:linear-gradient(200deg,#d83040 0%,rgba(160,122,56,0) 60%)" role="img" aria-label="Photo of Asian produce on woven bamboo mat"></div>
    <h2 style="top:44px">ASIAN SPECIALTIES</h2>
  </div>

  <nav class="tab-bar">
    <svg style="left:23px;color:#777"><use href="#i-home"/></svg>
    <svg style="left:86px;color:#777"><use href="#i-eye"/></svg>
    <svg style="left:148px;color:var(--green)"><use href="#i-apple"/></svg>
    <svg style="left:210px;color:#777"><use href="#i-bowl"/></svg>
    <svg style="left:268px;color:#777"><use href="#i-person"/></svg>
  </nav>
</section>

<!-- Produce detail screen -->
<section class="screen screen--detail">
  <div class="status-bar">
    <span class="carrier"><svg width="12" height="8"><use href="#i-signal"/></svg>Nimbus<svg width="12" height="9"><use href="#i-wifi"/></svg></span>
    <span class="clock">9:41 AM</span>
    <span class="power">58 %<svg width="24" height="11"><use href="#i-battery"/></svg></span>
  </div>
  <svg class="abs" style="top:27px;left:14px" width="18" height="14" viewBox="0 0 18 14"><path d="M17 7H2M7 1 1 7l6 6" fill="none" stroke="#5bcd3a" stroke-width="1.8"/></svg>
  <svg class="abs" style="top:22px;left:282px" width="20" height="20" viewBox="0 0 20 20"><circle cx="16" cy="4" r="2.5" fill="none" stroke="#999" stroke-width="1.2"/><circle cx="4" cy="10" r="2.5" fill="none" stroke="#999" stroke-width="1.2"/><circle cx="16" cy="16" r="2.5" fill="none" stroke="#999" stroke-width="1.2"/><path d="M6.2 9 13.8 5M6.2 11l7.6 4" stroke="#999" stroke-width="1.2"/></svg>
  <div class="abs" style="top:22px;left:30px;width:258px;height:170px;border-radius:45%;background:radial-gradient(ellipse,#d42a1c 0%,#c01a14 45%,rgba(255,255,255,0) 72%)" role="img" aria-label="Photo of a pile of red Holland bell peppers, one cut in half"></div>

  <div class="item-name">Red Holland Bell Peppers</div>
  <div class="item-meta">Inventory, 10 lbs : 0<br>Last sold on : 09/12/17</div>
  <div class="divider" style="top:269px;left:22px;right:22px"></div>

  <div class="stat" style="left:23px">
    <svg viewBox="0 0 24 24"><path d="M12 21S2 14 2 8a5 5 0 0 1 10-1 5 5 0 0 1 10 1c0 6-10 13-10 13z" fill="none" stroke="#5bcd3a" stroke-width="1.4"/></svg>
    <b>2.6 K</b><small>Favorites</small>
  </div>
  <div class="stat" style="left:91px">
    <svg viewBox="0 0 24 24"><path d="M3 3l18 18M21 3 3 21M6 2l-3 3 4 4 3-3M18 2l3 3" fill="none" stroke="#5bcd3a" stroke-width="1.4"/></svg>
    <b>6</b><small>Restaurants</small>
  </div>
  <div class="stat" style="left:159px">
    <svg viewBox="0 0 24 24" style="color:#5bcd3a"><use href="#i-bowl"/></svg>
    <b>7</b><small>Recipes</small>
  </div>
  <div class="stat" style="left:228px">
    <svg viewBox="0 0 24 24"><path d="M12 22s-7-7-7-13a7 7 0 0 1 14 0c0 6-7 13-7 13z" fill="none" stroke="#5bcd3a" stroke-width="1.4"/><circle cx="12" cy="9" r="2.5" fill="none" stroke="#5bcd3a" stroke-width="1.4"/></svg>
    <b>2</b><small>Spots</small>
  </div>

  <div class="description">
    <h3>Description/Taste</h3>
    <p>Red Holland bell peppers are a smooth-skinned variety with uniformly colored skin and a partial stem attached. Displaying three to four thick-walled lobes, the pepper has internal ribbing and seeds, which are discarded before use. Similar in flavor to a yellow or orange Holland bell pepper, the Red Holland bell has a mild, sweet pepper flavor with a crisp-firm texture. (Scoville units: 0-100).</p>
  </div>

  <nav class="tab-bar">
    <svg style="left:23px;color:#777"><use href="#i-home"/></svg>
    <svg style="left:86px;color:#777"><use href="#i-eye"/></svg>
    <svg style="left:148px;color:var(--green)"><use href="#i-apple"/></svg>
    <svg style="left:210px;color:#777"><use href="#i-bowl"/></svg>
    <svg style="left:268px;color:#777"><use href="#i-person"/></svg>
  </nav>
</section>

</body>
</html>
```